TALBRIDGE VENTORA

I'D LIKE TO REDESIGN MY WEBSITE TO MATCH WITH THE NEW BROCHURE WHICH IS ATTACHED. CONTENT AND LOGOS ARE ATTACHED. PLEASE USE WATCH BRAND LOGOS FROM THE BROCHURE
Coded - Design and coding required
1 page

```html
<!DOCTYPE html>
<html lang="en">
<head>
<meta charset="utf-8">
<title>Talbridge Ventora – International Luxury Timepiece Supplier</title>
<link rel="stylesheet" href="https://fonts.googleapis.com/css2?family=Poppins:wght@400;500;600;700&display=swap">
<style>
:root{
  --gold:#c29d36;
  --gold-light:#d4b253;
  --gold-dark:#a8862a;
  --black:#000;
  --white:#fff;
  --muted:#cfcfcf;
}
*{box-sizing:border-box;margin:0;padding:0}
html,body{width:1200px;height:3516px;overflow:hidden;background:var(--black)}
body{position:relative;font-family:"Poppins",sans-serif;color:var(--white)}
.abs{position:absolute}

/* Header */
.site-header{position:absolute;left:0;top:0;width:1200px;height:91px;background:var(--black)}
.brand{position:absolute;display:flex;align-items:center;gap:8px;font-weight:600;color:var(--gold);letter-spacing:.5px}
.brand-mark{width:12px;height:12px;background:var(--gold)}
.site-header .brand{left:140px;top:32px;font-size:15px}
.main-nav a{position:absolute;top:34px;font-size:15px;color:var(--white);text-decoration:none;letter-spacing:.3px}
.main-nav a.active{color:var(--gold);font-weight:600}
.main-nav a.active::after{content:"";position:absolute;left:0;right:0;top:27px;height:2px;background:var(--gold)}

/* Hero */
.hero{position:absolute;left:0;top:91px;width:1200px;height:616px;background:linear-gradient(100deg,#c9a53e 0%,#b89431 60%,#c7a23c 100%)}
.hero-photo{position:absolute;left:587px;top:0;width:613px;height:616px;background:radial-gradient(ellipse at 50% 45%,#5a7fb0 0%,#3f5f8c 40%,#b8973a 80%)}
.hero-frame{position:absolute;left:72px;top:77px;width:114px;height:456px;border:2px solid var(--white);border-right:none}
.hero-frame::before,.hero-frame::after{content:"";position:absolute;right:0;width:2px;height:26px;background:var(--white)}
.hero-frame::before{top:0}
.hero-frame::after{bottom:0}
.hero-title{position:absolute;left:124px;top:113px;width:440px;font-size:32px;line-height:44px;font-weight:600;text-transform:uppercase}
.hero-text{position:absolute;left:127px;top:296px;width:436px;font-size:13.5px;line-height:23px}
.hero-tagline{position:absolute;left:126px;top:441px;width:400px;font-size:18px;line-height:25px}

/* About */
.about{position:absolute;left:0;top:707px;width:1200px;height:745px;background:var(--black)}
.section-title{position:absolute;left:0;width:1200px;text-align:center;font-weight:600;font-size:32px;text-transform:uppercase}
.about .section-title{top:56px;color:var(--gold)}
.about-lead{position:absolute;left:222px;top:104px;width:756px;text-align:center;font-size:14px;line-height:25.6px}
.about-frame{position:absolute;left:192px;top:248px;width:368px;height:385px;border:2px solid var(--gold)}
.about-photo{position:absolute;left:9px;top:9px;width:346px;height:363px;background:linear-gradient(180deg,#1e2e6a 0%,#2b3c7a 55%,#c9ccd6 85%,#e4e5ea 100%)}
.about-body{position:absolute;left:610px;top:290px;width:445px;font-size:15px;line-height:25.6px}
.about-body p+p{margin-top:14px}

/* Investments */
.investments{position:absolute;left:0;top:1452px;width:1200px;height:328px;background:linear-gradient(90deg,#c09b36,#b8952f 50%,#c6a23d)}
.investments .section-title{top:88px;color:var(--white)}
.investments p{position:absolute;left:0;width:1200px;text-align:center;font-size:15px;line-height:26px}

/* Search */
.search{position:absolute;left:0;top:1780px;width:1200px;height:556px;background:var(--black)}
.search .section-title{top:78px}
.search-field{position:absolute;width:367px;height:57px;border:2px solid var(--white);font-size:16px;font-weight:500;padding:0 22px;display:flex;align-items:center;justify-content:space-between}
.search-button{position:absolute;left:504px;top:386px;width:191px;height:52px;background:var(--white);color:var(--gold);font-size:22px;font-weight:600;display:flex;align-items:center;justify-content:center}

/* Contact */
.contact{position:absolute;left:0;top:2336px;width:1200px;height:742px;background:linear-gradient(135deg,#c6a23d 0%,#b8952f 55%,#c8a540 100%)}
.contact-title{position:absolute;left:162px;top:176px;font-size:38px;font-weight:500}
.contact-intro{position:absolute;left:163px;top:233px;font-size:14px;line-height:27px}
.contact-item{position:absolute;left:159px;display:flex;align-items:center;gap:16px}
.contact-icon{width:50px;height:50px;border-radius:50%;background:var(--white);display:flex;align-items:center;justify-content:center}
.contact-item strong{display:block;font-size:19px;font-weight:500}
.contact-item span{display:block;font-size:18px}
.contact-form{position:absolute;left:640px;top:94px;width:436px;height:550px;background:var(--white)}
.form-field{position:absolute;left:47px;width:335px;height:52px;border:2px solid var(--gold);color:#7a7a7a;font-size:17px;padding:12px 12px}
.form-submit{position:absolute;left:49px;top:467px;width:148px;height:35px;border:2px solid #222;color:#111;font-size:14px;font-weight:600;display:flex;align-items:center;justify-content:center}

/* Footer */
.site-footer{position:absolute;left:0;top:3078px;width:1200px;height:378px;background:var(--black)}
.site-footer .brand{left:120px;top:170px;font-size:17px}
.socials{position:absolute;left:122px;top:243px;display:flex;gap:16px}
.socials span{width:30px;height:30px;border-radius:50%;background:var(--gold)}
.footer-col{position:absolute;top:97px;border-left:3px solid var(--gold);padding-left:16px}
.footer-col h3{font-size:17px;font-weight:600;margin-top:-8px}
.footer-col h4{font-size:13px;font-weight:600;margin-top:-6px}
.footer-col a{display:block;color:var(--muted);text-decoration:none;font-size:14px;line-height:29.5px}
.footer-col a.active{color:var(--gold)}
.footer-contact li{list-style:none;display:flex;align-items:center;gap:12px;font-size:12px;color:var(--muted);margin-bottom:10px}
.footer-contact .dot{width:33px;height:33px;border-radius:50%;background:var(--gold);display:flex;align-items:center;justify-content:center}
.copyright{position:absolute;left:0;top:3456px;width:1200px;height:60px;background:var(--gold);text-align:center;line-height:60px;font-size:11px;color:#f2e6c2}
</style>
</head>
<body>

<header class="site-header">
  <div class="brand"><span class="brand-mark"></span>TALBRIDGE VENTORA</div>
  <nav class="main-nav">
    <a class="active" style="left:466px">HOME</a>
    <a style="left:550px">ABOUT US</a>
    <a style="left:665px">INVESTMENTS</a>
    <a style="left:805px">SEARCH WATCHES</a>
    <a style="left:976px">CONTACT US</a>
  </nav>
</header>

<section class="hero">
  <div class="hero-photo" role="img" aria-label="Man in a blue suit holding a silver chronograph watch"></div>
  <div class="hero-frame"></div>
  <h1 class="hero-title">Welcome to Talbridge Ventora International Luxury Timepiece Supplier</h1>
  <p class="hero-text">Simply choose a desired product and allow us to source it for you at the best price and with suitable delivery terms. You will have an option to either collect your purchase from our Cheshire based boutique store, collection points are also in New York City or Dubai or get it delivered to your door via one of our fully insured couriers.</p>
  <p class="hero-tagline">Making your luxury shopping experience as simple as it can be.</p>
</section>

<section class="about">
  <h2 class="section-title">About Us</h2>
  <p class="about-lead">Talbridge Ventora was first founded in 2018, it has been established as the premier resource to buy and sell premium pre-owned watches. With thousands of watches available from brands including Halvorsen, Arden Marchetti, Veltrane Sorel, Maxence Dufort, Orlian, Castellane and more, plus international locations and clients there’s no better place to find a luxury timepiece.as</p>
  <div class="about-frame">
    <div class="about-photo" role="img" aria-label="Two-tone gold and silver dress watch on a navy backdrop"></div>
  </div>
  <div class="about-body">
    <p>Outstanding customer service is a mainstay of the Talbridge ethos. Watch collectors are discerning shoppers, and will accept nothing but the best, which is why customer service has and always will be such an important part of the business.</p>
    <p>Our dedicated team of swiss watch experts are perfectly placed to adapt to the ever changing market conditions, giving our investors an ‘out of the box’ solution. Longevity is as much a focus as immediate success, ensuring you have the best options we can provide tomorrow as well as</p>
  </div>
</section>

<section class="investments" role="img" aria-label="Gold-toned background of watch details">
  <h2 class="section-title">Investments</h2>
  <p style="top:140px">Interested in becoming part of the ever growing Talbridge Ventora?</p>
  <p style="top:179px">Please leave your details contact form below and one of the team will be in<br>touch to discuss potential options.</p>
</section>

<section class="search">
  <h2 class="section-title">Search Watches</h2>
  <div class="search-field" style="left:220px;top:143px">Watch Brand<svg width="18" height="10" viewBox="0 0 18 10"><path d="M1 1l8 7 8-7" fill="none" stroke="#fff" stroke-width="2"/></svg></div>
  <div class="search-field" style="left:610px;top:143px">Year<svg width="18" height="10" viewBox="0 0 18 10"><path d="M1 1l8 7 8-7" fill="none" stroke="#fff" stroke-width="2"/></svg></div>
  <div class="search-field" style="left:220px;top:220px">Material<svg width="18" height="10" viewBox="0 0 18 10"><path d="M1 1l8 7 8-7" fill="none" stroke="#fff" stroke-width="2"/></svg></div>
  <div class="search-field" style="left:610px;top:220px">Bezel<svg width="18" height="10" viewBox="0 0 18 10"><path d="M1 1l8 7 8-7" fill="none" stroke="#fff" stroke-width="2"/></svg></div>
  <div class="search-field" style="left:220px;top:295px">Strap<svg width="18" height="10" viewBox="0 0 18 10"><path d="M1 1l8 7 8-7" fill="none" stroke="#fff" stroke-width="2"/></svg></div>
  <div class="search-field" style="left:610px;top:295px">Description</div>
  <div class="search-button">SEARCH</div>
</section>

<section class="contact">
  <h2 class="contact-title">CONTACT US</h2>
  <p class="contact-intro">Alternatively please feel free to contact us on 01619047732<br>For a more detailed chat with one of our timepiece specialists</p>
  <div class="contact-item" style="top:328px">
    <div class="contact-icon"><svg width="22" height="28" viewBox="0 0 22 28"><path d="M11 1a10 10 0 0 0-10 10c0 7 10 16 10 16s10-9 10-16A10 10 0 0 0 11 1z" fill="#c29d36"/><circle cx="11" cy="11" r="4" fill="#fff"/></svg></div>
    <div><strong>Address :-</strong><span>TBC</span></div>
  </div>
  <div class="contact-item" style="top:412px">
    <div class="contact-icon"><svg width="26" height="18" viewBox="0 0 26 18"><rect x="1" y="1" width="24" height="16" fill="#c29d36"/><path d="M1 1l12 9 12-9" fill="none" stroke="#fff" stroke-width="2"/></svg></div>
    <div><strong>Email :-</strong><span>sales@talbridge-ventora.co.uk</span></div>
  </div>
  <div class="contact-item" style="top:493px">
    <div class="contact-icon"><svg width="24" height="24" viewBox="0 0 24 24"><path d="M6 2l4 5-2 3c1 3 3 5 6 6l3-2 5 4-2 4C10 22 2 14 2 5z" fill="#c29d36"/></svg></div>
    <div><strong>Phone :-</strong><span>01619047732</span></div>
  </div>

  <form class="contact-form">
    <div class="form-field" style="top:46px">First name*</div>
    <div class="form-field" style="top:108px">Last name</div>
    <div class="form-field" style="top:170px">Phone*</div>
    <div class="form-field" style="top:232px">Email address*</div>
    <div class="form-field" style="top:295px;height:154px">Message</div>
    <div class="form-submit">SUBMIT NOW</div>
  </form>
</section>

<footer class="site-footer">
  <div class="brand"><span class="brand-mark"></span>TALBRIDGE VENTORA</div>
  <div class="socials"><span></span><span></span><span></span><span></span></div>

  <div class="footer-col" style="left:392px">
    <h3>Navigation</h3>
    <div style="margin-top:6px">
      <a class="active">Home</a><a>About us</a><a>Investments</a><a>Search Watches</a><a>Contact us</a>
    </div>
  </div>
  <div class="footer-col" style="left:632px">
    <h4>Other Links</h4>
    <div style="margin-top:8px;padding-left:3px"><a>Terms &amp; Conditions</a><a>Prvacy Policy</a></div>
  </div>
  <div class="footer-col" style="left:838px">
    <h4 style="padding-left:6px">Contact Information</h4>
    <ul class="footer-contact" style="margin-top:10px;padding-left:26px;margin-left:-26px">
      <li><span class="dot"><svg width="12" height="16" viewBox="0 0 22 28"><path d="M11 1a10 10 0 0 0-10 10c0 7 10 16 10 16s10-9 10-16A10 10 0 0 0 11 1z" fill="#fff"/></svg></span>TBC</li>
      <li><span class="dot"><svg width="14" height="14" viewBox="0 0 24 24"><path d="M6 2l4 5-2 3c1 3 3 5 6 6l3-2 5 4-2 4C10 22 2 14 2 5z" fill="#fff"/></svg></span>+01619047732</li>
      <li><span class="dot"><svg width="16" height="11" viewBox="0 0 26 18"><rect x="1" y="1" width="24" height="16" fill="#fff"/><path d="M1 1l12 9 12-9" fill="none" stroke="#c29d36" stroke-width="2"/></svg></span>sales@talbridge-ventora.co.uk</li>
    </ul>
  </div>
</footer>

<div class="copyright">© 2022 TALBRIDGE-VENTORA.CO.UK ALL RIGHT RESERVED</div>

</body>
</html>
```